Boat business cards

I'm looking for business cards with the two logos I've attached. I don't have an specific idea in mind and open to anything. All the usual info will be on the card. Name, position in company, nr, email, address, ect. The company rents out these two boats for charters and fishing.

```html
<!DOCTYPE html>
<html lang="en">
<head>
<meta charset="utf-8">
<title>Harbor Wake – Business Cards</title>
<link rel="stylesheet" href="https://fonts.googleapis.com/css2?family=Open+Sans:wght@400;600&display=swap">
<style>
  :root{
    --stage:#d9d9d9;
    --ink:#1c1c1e;
    --card-white:#ffffff;
    --card-black:#151515;
    --ocean:#1f8bcc;
    --ocean-deep:#1674b0;
    --silver:#c6c8ca;
    --gold:#a58d66;
    --muted:#555a60;
    --light:#ffffff;
  }
  *{box-sizing:border-box;margin:0;padding:0}
  html,body{width:1200px;height:675px;overflow:hidden}
  body{
    background:var(--stage);
    font-family:"Open Sans",Arial,sans-serif;
    position:relative;
  }
  .card{
    position:absolute;
    top:189px;
    width:520px;height:297px;
    border-radius:18px;
    overflow:hidden;
    box-shadow:0 10px 24px rgba(0,0,0,.18);
  }
  .card svg.waves{position:absolute;inset:0;width:100%;height:100%}
  .card--back{left:50px;background:var(--card-black)}
  .card--front{left:630px;background:var(--card-white)}

  .wordmark{
    position:absolute;
    font-weight:600;
    letter-spacing:.04em;
    white-space:nowrap;
  }
  .card--back .wordmark{
    left:0;right:0;top:112px;text-align:center;
    font-size:32px;color:var(--light);
  }
  .card--front .wordmark{
    left:196px;top:70px;font-size:28px;color:var(--ink);
  }

  .contact-block{
    position:absolute;left:22px;top:26px;
    color:var(--light);font-size:12px;line-height:17px;
  }
  .contact-row{display:flex;align-items:flex-start;gap:8px}
  .contact-row svg{width:11px;height:11px;margin-top:3px;flex:none;fill:var(--light)}
  .contact-row + .contact-row{margin-top:2px}

  .identity{
    position:absolute;right:30px;top:158px;text-align:right;
  }
  .identity .person-name{font-size:19px;color:var(--gold);letter-spacing:.04em;line-height:22px}
  .identity .person-role{font-size:11px;color:var(--muted)}

  .online-block{
    position:absolute;right:20px;top:238px;
    color:var(--light);font-size:12px;line-height:18px;text-align:right;
  }
  .online-block .contact-row{justify-content:flex-end;flex-direction:row-reverse}
  .online-block .contact-row svg{margin-top:4px}
</style>
</head>
<body>

<section class="card card--back" aria-label="Card back">
  <svg class="waves" viewBox="0 0 520 297" preserveAspectRatio="none" aria-hidden="true">
    <path d="M0,168 C120,150 250,190 380,235 C440,256 490,270 520,268 L520,297 L0,297 Z" fill="var(--silver)"/>
    <path d="M0,176 C120,160 250,198 380,243 C440,262 490,276 520,275 L520,297 L0,297 Z" fill="var(--card-black)"/>
    <path d="M0,184 C125,170 255,206 385,250 C445,268 490,282 520,282 L520,297 L0,297 Z" fill="var(--light)"/>
    <path d="M0,190 C125,178 255,214 385,258 C445,276 490,288 520,288 L520,297 L0,297 Z" fill="var(--card-black)"/>
    <path d="M0,196 C130,186 260,224 390,268 C440,284 480,294 520,297 L0,297 Z" fill="var(--ocean)"/>
  </svg>
  <div class="wordmark">HARBOR WAKE</div>
</section>

<section class="card card--front" aria-label="Card front">
  <svg class="waves" viewBox="0 0 520 297" preserveAspectRatio="none" aria-hidden="true">
    <path d="M0,0 L168,0 C178,110 270,200 520,222 L520,297 L0,297 Z" fill="var(--silver)"/>
    <path d="M0,0 L156,0 C166,116 262,208 520,231 L520,297 L0,297 Z" fill="var(--light)"/>
    <path d="M0,0 L150,0 C160,120 258,214 520,236 L520,297 L0,297 Z" fill="var(--ocean)"/>
    <path d="M0,282 C200,292 400,290 520,270 L520,297 L0,297 Z" fill="var(--ocean-deep)" opacity=".35"/>
  </svg>

  <div class="contact-block">
    <div class="contact-row">
      <svg viewBox="0 0 12 12"><path d="M6 0a4 4 0 0 0-4 4c0 3 4 8 4 8s4-5 4-8a4 4 0 0 0-4-4zm0 5.6A1.6 1.6 0 1 1 6 2.4a1.6 1.6 0 0 1 0 3.2z"/></svg>
      <div>Address Line 1<br>Address Line 2</div>
    </div>
    <div class="contact-row">
      <svg viewBox="0 0 12 12"><path d="M2.5 0.5l2 2-1.2 1.6c.8 1.7 2 2.9 3.6 3.6l1.6-1.2 2 2-1.3 2.5C4.6 10.8 1.2 7.4 0 2.9z"/></svg>
      <div>000 000 0000</div>
    </div>
    <div class="contact-row">
      <svg viewBox="0 0 12 12"><path d="M2.5 0.5l2 2-1.2 1.6c.8 1.7 2 2.9 3.6 3.6l1.6-1.2 2 2-1.3 2.5C4.6 10.8 1.2 7.4 0 2.9z"/></svg>
      <div>000 000 0000</div>
    </div>
  </div>

  <div class="wordmark">HARBOR WAKE</div>

  <div class="identity">
    <div class="person-name">NAME</div>
    <div class="person-role">Designation</div>
  </div>

  <div class="online-block">
    <div class="contact-row">
      <svg viewBox="0 0 12 12"><path d="M0 2h12v8H0zM1 3v.4l5 3.3 5-3.3V3zm0 1.6V9h10V4.6L6 7.9z"/></svg>
      <div>hello@harborwake.example</div>
    </div>
    <div class="contact-row">
      <svg viewBox="0 0 12 12"><path d="M6 0a6 6 0 1 0 0 12A6 6 0 0 0 6 0zm0 1c.7 0 1.5 1.5 1.7 4H4.3C4.5 2.5 5.3 1 6 1zM1 6.5h2.3c.1 1.5.4 2.9 1 3.9A5 5 0 0 1 1 6.5zm0-1a5 5 0 0 1 3.3-3.9c-.6 1-.9 2.4-1 3.9zM6 11c-.7 0-1.5-1.5-1.7-4.5h3.4C7.5 9.5 6.7 11 6 11zm1.7-.6c.6-1 .9-2.4 1-3.9H11a5 5 0 0 1-3.3 3.9zM8.7 5.5c-.1-1.5-.4-2.9-1-3.9A5 5 0 0 1 11 5.5z"/></svg>
      <div>harborwake.example</div>
    </div>
  </div>
</section>

</body>
</html>
```